Car rental website design for a UAE car rental company

This project is about creating a new website design for a car rental company located in Dubai (United Arab Emirates), I opened the same project a few months ago but I didn't receive a lot of appealing entries so I closed it but this time I am marking the project as guaranteed to avoid such situation again, if you have already provided a design before then please re-submit again on this project so that it is considered while reviewing all the designs

A few important things:

1- We need a simple non-complex design
2- The final deliverable would be 2 screens (PSD, JPEG ... etc), the first screen is for the home page and the second screen is for an internal page
3- The home page must have a section that end users can use to rent a car online directly from the home page instead of going into some inner pages
4- The current website is very old and not very appealing so avoid creating a similar design (www.quarvin-drive.example)
5- The name is Quarvin but the company rents normal cars (no Limousin cars will be rented) so avoid adding any fancy cars in the images/graphics used in the design, just normal end users cars
6- The expected pages would be: home, About us, Our team, Strategy, Contact us and links to social media pages
7- The attachments include the company's logo and some screens from other car rental companies that provide online rentals/payments

If you have any questions please feel free to ask and please note that we will need the designs urgently

Thanks

Target Market(s)

Dubai - United Arab Emirates

Industry/Entity Type

It Company

Number of Pages Required

2 page

Font styles to use
Sans Serif

Requirements
Must have
• Check the project details
Nice to have
Should not have

```html
<!DOCTYPE html>
<html lang="en">
<head>
<meta charset="utf-8">
<title>Quarvin – Rent A Car</title>
<link rel="stylesheet" href="https://fonts.googleapis.com/css2?family=Open+Sans:wght@300;400;600&family=Arimo:wght@400&display=swap">
<style>
  :root {
    --ink: #4a4a4a;
    --muted: #8c8c8c;
    --accent-red: #b3123f;
    --phone-red: #d4373b;
    --gold: #e9c81e;
    --gold-text: #f0c419;
    --about-band: #6e7872;
    --card-bg: #f2f2f2;
    --icon-grey: #7b807d;
    --footer-bg: #3b3b3b;
    --rule: #e3e3e3;
    --white: #ffffff;
  }
  * { margin: 0; padding: 0; box-sizing: border-box; }
  html, body { width: 1200px; height: 900px; overflow: hidden; background: var(--white); }
  body { position: relative; font-family: "Open Sans", Arial, sans-serif; color: var(--ink); }
  .abs { position: absolute; }

  /* header */
  .brand { left: 312px; top: 10px; display: flex; align-items: center; gap: 6px; }
  .brand-square { width: 18px; height: 18px; background: var(--accent-red); }
  .brand-name { font-size: 15px; font-weight: 600; color: var(--accent-red); }
  .call { right: 376px; top: 7px; font-size: 10px; line-height: 14px; color: var(--phone-red); white-space: nowrap; }
  .social { top: 6px; width: 14px; height: 14px; border: 1px solid #bdbdbd; }
  .main-nav { right: 312px; top: 30px; display: flex; gap: 15px; font-size: 7px; text-transform: uppercase; color: #555; }

  /* hero */
  .hero { left: 194px; top: 51px; width: 812px; height: 320px; overflow: hidden;
    background: linear-gradient(180deg, #4a4a5e 0%, #8a6a58 38%, #c98a4c 55%, #3a2e28 75%, #1e1b1a 100%); }
  .hero-title { left: 117px; top: 56px; color: var(--white); }
  .hero-title h1 { font-size: 22px; font-weight: 300; letter-spacing: .2px; line-height: 28px; white-space: nowrap; }
  .hero-title p { font-size: 12.6px; font-weight: 300; line-height: 15px; white-space: nowrap; }
  .slide-arrow { top: 126px; width: 20px; height: 59px; background: rgba(200,200,200,.5); color: #555; font-size: 11px; display: flex; align-items: center; justify-content: center; }
  .slide-prev { left: 0; } .slide-next { right: 0; }

  .booking { left: 529px; top: 65px; width: 165px; height: 255px; background: rgba(40,34,30,.82); }
  .booking h2 { position: absolute; left: 0; right: 0; top: 12px; text-align: center; font-size: 12px; font-weight: 400; color: var(--gold-text); }
  .field { position: absolute; background: var(--white); border-radius: 2px; font-size: 7.5px; color: #999; padding: 4px 6px; height: 18px; }
  .field-from { left: 8px; top: 41px; width: 149px; }
  .field-to { left: 8px; top: 67px; width: 149px; }
  .field-date { left: 8px; width: 67px; }
  .field-date svg { position: absolute; right: 3px; top: 3px; }
  .option { position: absolute; left: 81px; font-size: 7.5px; color: var(--white); display: flex; align-items: center; gap: 4px; white-space: nowrap; }
  .option i { display: block; width: 6px; height: 6px; background: var(--white); }
  .book-now { position: absolute; left: 37px; top: 151px; width: 94px; height: 19px; background: var(--gold); font-size: 9px; color: #333; display: flex; align-items: center; justify-content: center; }

  /* about */
  .about { left: 194px; top: 371px; width: 812px; height: 96px; background: var(--about-band); color: var(--white); }
  .about-heading { right: 613px; top: 26px; text-align: right; font-weight: 400; line-height: 18px; }
  .about-heading span { display: block; font-size: 15px; }
  .about-heading strong { display: block; font-size: 19px; font-weight: 400; }
  .about-rule { left: 213px; top: 14px; width: 1px; height: 68px; background: rgba(255,255,255,.35); }
  .about-text { left: 228px; top: 21px; width: 462px; font-family: Arimo, Arial, sans-serif; font-size: 7px; line-height: 13.2px; }

  /* features */
  .feature { top: 490px; width: 135px; height: 183px; background: var(--card-bg); border-radius: 4px; text-align: center; }
  .feature svg { position: absolute; left: 40px; top: 8px; }
  .feature h3 { position: absolute; left: 0; right: 0; top: 70px; font-size: 15px; font-weight: 300; color: #555; }
  .feature p { position: absolute; left: 12px; right: 12px; top: 99px; font-family: Arimo, Arial, sans-serif; font-size: 6.6px; line-height: 12.2px; color: var(--muted); }
  .more { position: absolute; left: 46px; top: 156px; width: 43px; height: 17px; background: var(--accent-red); color: var(--white); font-size: 8.5px; display: flex; align-items: center; justify-content: center; border-radius: 1px; }

  /* lower columns */
  .column { top: 697px; width: 136px; }
  .column h3 { font-size: 15px; font-weight: 300; color: #444; line-height: 18px; white-space: nowrap; }
  .column-photo { margin-top: 11px; width: 135px; height: 66px; }
  .column p { margin-top: 6px; font-family: Arimo, Arial, sans-serif; font-size: 6.4px; line-height: 12.2px; color: #555; text-align: justify; }
  .capabilities { list-style: none; margin-top: 4px; }
  .capabilities li { height: 24.5px; border-bottom: 1px solid var(--rule); display: flex; align-items: center; gap: 9px; font-family: Arimo, Arial, sans-serif; font-size: 7px; color: #aaa; white-space: nowrap; }
  .capabilities li i { width: 11px; height: 11px; border-radius: 50%; background: var(--gold); position: relative; flex: none; }
  .capabilities li i::after { content: ""; position: absolute; left: 3px; top: 3px; width: 3px; height: 3px; border-top: 1.2px solid #fff; border-right: 1.2px solid #fff; transform: rotate(45deg); }

  /* footer */
  .site-footer { left: 194px; top: 866px; width: 812px; height: 34px; background: var(--footer-bg); color: var(--white); font-size: 7px; }
  .footer-nav { left: 118px; top: 12px; display: flex; gap: 9px; text-transform: uppercase; }
  .copyright { right: 119px; top: 11px; white-space: nowrap; }
</style>
</head>
<body>

<header>
  <div class="abs brand"><span class="brand-square"></span><span class="brand-name">Quarvin</span></div>
  <div class="abs call">Call : +971 4 555 0182</div>
  <span class="abs social" style="left:834px"></span>
  <span class="abs social" style="left:853px"></span>
  <span class="abs social" style="left:873px"></span>
  <nav class="abs main-nav"><span>Home</span><span>About Us</span><span>Our Team</span><span>Strategy</span><span>Contact Us</span></nav>
</header>

<section class="abs hero" role="img" aria-label="City skyline at dusk with a road curving towards it and a dark family car on the right">
  <div class="abs hero-title">
    <h1>EXPERIENCE AN EXTRA MILE</h1>
    <p>OF COMFORT, PLEASURE AND LEISURE FROM THE BEST</p>
  </div>
  <div class="abs slide-arrow slide-prev">‹</div>
  <div class="abs slide-arrow slide-next">›</div>

  <form class="abs booking">
    <h2>Search &amp; Book Your Cab</h2>
    <div class="field field-from">From</div>
    <div class="field field-to">To</div>
    <div class="field field-date" style="top:94px">Departure
      <svg width="13" height="12" viewBox="0 0 13 12"><rect x=".5" y="1.5" width="12" height="10" fill="none" stroke="#555"/><rect x=".5" y="1.5" width="12" height="2.5" fill="#555"/><g fill="#555"><rect x="2.5" y="5.5" width="2" height="1.5"/><rect x="5.5" y="5.5" width="2" height="1.5"/><rect x="8.5" y="5.5" width="2" height="1.5"/><rect x="2.5" y="8.5" width="2" height="1.5"/><rect x="5.5" y="8.5" width="2" height="1.5"/><rect x="8.5" y="8.5" width="2" height="1.5"/></g></svg>
    </div>
    <div class="option" style="top:99px"><i></i>One Way</div>
    <div class="field field-date" style="top:120px">Return
      <svg width="13" height="12" viewBox="0 0 13 12"><rect x=".5" y="1.5" width="12" height="10" fill="none" stroke="#555"/><rect x=".5" y="1.5" width="12" height="2.5" fill="#555"/><g fill="#555"><rect x="2.5" y="5.5" width="2" height="1.5"/><rect x="5.5" y="5.5" width="2" height="1.5"/><rect x="8.5" y="5.5" width="2" height="1.5"/><rect x="2.5" y="8.5" width="2" height="1.5"/><rect x="5.5" y="8.5" width="2" height="1.5"/><rect x="8.5" y="8.5" width="2" height="1.5"/></g></svg>
    </div>
    <div class="option" style="top:125px"><i></i>Flexible dates</div>
    <div class="book-now">Book Now</div>
  </form>
</section>

<section class="abs about">
  <h2 class="abs about-heading"><span>About</span><strong>Quarvin</strong></h2>
  <div class="abs about-rule"></div>
  <p class="abs about-text">Lorem Ipsum is simply dummy text of the printing and typesetting industry. Lorem Ipsum has been the industry's standard dummy text ever since the 1500s, when an unknown printer took a galley of type and scrambled it to make a type specimen book. It has survived not only five centuries, but also the leap into electronic typesetting, remaining essentially unchanged. It was popularised in the 1960s with the release of Letraset sheets containing Lorem Ipsum passages, and more recently with desktop publishing software like Aldus PageMaker including versions of Lorem Ipsum.</p>
</section>

<section class="abs feature" style="left:312px">
  <svg width="55" height="55" viewBox="0 0 55 55"><circle cx="27.5" cy="29" r="24" fill="none" stroke="var(--icon-grey)" stroke-width="4"/><circle cx="27.5" cy="29" r="17" fill="none" stroke="var(--icon-grey)" stroke-width="2"/><path d="M27.5 18v11l7 5" fill="none" stroke="var(--icon-grey)" stroke-width="2.5" stroke-linecap="round"/></svg>
  <h3>Fast Booking</h3>
  <p>Lorem Ipsum is simply dummy text of the printing and typesetting industry. Lorem Ipsum of type and scrambled it to make a type.</p>
  <span class="more">MORE</span>
</section>
<section class="abs feature" style="left:459px">
  <svg width="55" height="55" viewBox="0 0 55 55"><rect x="5" y="22" width="38" height="30" rx="5" fill="var(--icon-grey)"/><rect x="30" y="32" width="13" height="10" rx="2" fill="var(--card-bg)"/><path d="M18 24c2-10 12-14 22-14V3l13 12-13 12v-8c-8 0-14 2-17 5z" fill="var(--icon-grey)"/></svg>
  <h3>Best Tariffs</h3>
  <p>Lorem Ipsum is simply dummy text of the printing and typesetting industry. Lorem Ipsum of type and scrambled it to make a type.</p>
  <span class="more">MORE</span>
</section>
<section class="abs feature" style="left:606px">
  <svg width="55" height="55" viewBox="0 0 55 55"><path d="M13 14a11 11 0 0 1 11 11c0 8-11 20-11 20S2 33 2 25a11 11 0 0 1 11-11z" fill="var(--icon-grey)"/><circle cx="13" cy="25" r="4.5" fill="var(--card-bg)"/><path d="M45 5a8 8 0 0 1 8 8c0 6-8 14-8 14s-8-8-8-14a8 8 0 0 1 8-8z" fill="var(--icon-grey)"/><circle cx="45" cy="13" r="3" fill="var(--card-bg)"/><path d="M22 44l14-8-8-3 16-8" fill="none" stroke="var(--icon-grey)" stroke-width="4" stroke-linejoin="round"/></svg>
  <h3>Best Routes</h3>
  <p>Lorem Ipsum is simply dummy text of the printing and typesetting industry. Lorem Ipsum of type and scrambled it to make a type.</p>
  <span class="more">MORE</span>
</section>
<section class="abs feature" style="left:752px">
  <svg width="55" height="55" viewBox="0 0 55 55"><rect x="23" y="1" width="9" height="5" rx="1" fill="var(--icon-grey)"/><rect x="26" y="5" width="3" height="5" fill="var(--icon-grey)"/><circle cx="27.5" cy="32" r="20" fill="none" stroke="var(--icon-grey)" stroke-width="4"/><path d="M27.5 18l-3 16h6z" fill="var(--icon-grey)"/><circle cx="27.5" cy="33" r="3" fill="var(--icon-grey)"/></svg>
  <h3>Fast &amp; Safe</h3>
  <p>Lorem Ipsum is simply dummy text of the printing and typesetting industry. Lorem Ipsum of type and scrambled it to make a type.</p>
  <span class="more">MORE</span>
</section>

<section class="abs column" style="left:311px">
  <h3>Company Profile</h3>
  <div class="column-photo" role="img" aria-label="Open company brochure on a yellow background" style="background:linear-gradient(120deg,#e7c51c 0%,#caa918 30%,#e9e7e3 55%,#8d9299 100%)"></div>
  <p>Lorem Ipsum is simply dummy text of the printing and typesetting industry. Lorem Ipsum of type and scrambled it to make a type.</p>
</section>
<section class="abs column" style="left:458px">
  <h3>Driver Services</h3>
  <div class="column-photo" role="img" aria-label="Gloved hand of a driver holding a car door handle" style="background:linear-gradient(110deg,#2a2c2f 0%,#6b7075 45%,#d9dadb 60%,#3a3d40 100%)"></div>
  <p>Lorem Ipsum is simply dummy text of the printing and typesetting industry. Lorem Ipsum of type and scrambled it to make a type.</p>
</section>
<section class="abs column" style="left:605px">
  <h3>Where We Go</h3>
  <div class="column-photo" role="img" aria-label="Hands on a steering wheel while driving" style="background:linear-gradient(100deg,#1f2326 0%,#50565b 40%,#b9bcbe 65%,#2c3034 100%)"></div>
  <p>Lorem Ipsum is simply dummy text of the printing and typesetting industry. Lorem Ipsum of type and scrambled it to make a type.</p>
</section>
<section class="abs column" style="left:753px">
  <h3>Capabilities</h3>
  <ul class="capabilities">
    <li><i></i>24 hours, 7 days a week</li>
    <li><i></i>Airport Service</li>
    <li><i></i>Priority Delivery Service</li>
    <li><i></i>Senior Discounts</li>
    <li><i></i>Wheelchair Accessible Cabs</li>
  </ul>
</section>

<footer class="abs site-footer">
  <nav class="abs footer-nav"><span>Home</span><span>|</span><span>About Us</span><span>|</span><span>Our Team</span><span>|</span><span>Strategy</span><span>|</span><span>Contact Us</span></nav>
  <div class="abs copyright">© Copyright 2011, Quarvin. All rights reserved.</div>
</footer>

</body>
</html>
```